Etiketten für Fruchtaufstriche eines Hofladens
Zielgruppe
Wir sind der Lindqvisthof Hofladen (www.lindqvisthof-beispiel.de), ein regionaler Erzeuger und Händler hochwertiger Lebensmittel. Für unsere hausgemachten Fruchtaufstriche suchen wir ein neues schönes Etikett das auch hochwertig wirkt. Die Produkte sind eher hochpreisig und hochwertig. Das Etikett sollte daher auch nicht irgendwie 'billig' wirken.
Aufgabenstellung
Wie bereits schon erwähnt, sollte das Etikett hochwertig wirken. Als Endformat stellen wir uns eine Breite von 95mm und eine Höhe von 60mm vor. Siehe hierzu die Vorlage der Druckerei im Anhang (bitte Beschnitt von 6mm beachten). Es wird ein ganz normales rundes Glas verwendet.
Bitte beachten Sie, dass wir kein industrieller Hersteller sind sondern eine kleine Manufaktur. Damit die verschiedenen Sorten einfach zu erkennen sind, wäre beispielsweise eine Erdbeere (farbig) auf schön. Bei anderen Sorten, wie beispielsweise bei einem Himbeer Fruchtaufstrich, gegen eine Himbeere ausgetauscht werden. Das Etikett sollte später auch anpassbar sein, immer wieder ändern sich Vorschriften zur Deklaration, diese wollen wir selbst einfach anpassen können. Außerdem soll das Etikett in Zukunft auch einfach und spontan auf weitere Sorten Fruchtaufstrich anpassbar sein, hierzu müssen wir selbst die Zutatenliste und natürlich den Titel ändern können. Deshalb ist es wichtig, dass wir am Ende ein InDesign Format zur Verfügung haben.
Was soll auf das Etikett:
Bezeichnung:
Erdbeer Fruchtaufstrich
Hersteller:
Lindqvisthof Hofladen GbR
Bernd und Carola Wessling
Obere Kastanienallee 17
83719 Rainfeld
Logo:
siehe Datei
Inhalt:
275ml
Zutaten:
Erdbeeren, Gelierzucker 2:1, Zitronensäure
Haltbarkeit:
mindestens haltbar bis: siehe Boden
Internetadresse:
www.lindqvisthof-beispiel.de

```html
<!DOCTYPE html>
<html lang="de">
<head>
<meta charset="utf-8">
<title>Lindqvisthof Fruchtaufstrich Etiketten</title>
<link rel="stylesheet" href="https://fonts.googleapis.com/css2?family=Quicksand:wght@400;500;600&family=Sacramento&display=swap">
<style>
  :root {
    --paper: #ffffff;
    --outer-line: #222222;
    --trim-line: #8c8c8c;
    --brown: #a57c45;
    --ink: #2a2a2a;
    --strawberry: #d5232f;
    --blueberry: #5b8fcf;
    --ring: #c9dbab;
    --ring-soft: #e2ecd2;
    --disc: #dde8c8;
  }
  * { margin: 0; padding: 0; box-sizing: border-box; }
  html, body { width: 1200px; height: 912px; overflow: hidden; background: var(--paper); }
  body { position: relative; font-family: "Quicksand", sans-serif; color: var(--ink); }

  .bleed-frame { position: absolute; top: 151px; width: 347px; height: 549px; border: 2px solid var(--outer-line); }
  .bleed-frame--strawberry { left: 129px; }
  .bleed-frame--blueberry { left: 673px; }

  .label { position: absolute; top: 186px; width: 277px; height: 479px; border: 2px solid var(--trim-line); }
  .label--strawberry { left: 164px; }
  .label--blueberry { left: 709px; }

  .fruit-art { position: absolute; z-index: 1; }
  .label--strawberry .fruit-art {
    left: 165px; top: 22px; width: 122px; height: 154px;
    background:
      radial-gradient(ellipse 42% 20% at 58% 17%, rgba(104,146,58,0.95) 0%, rgba(120,160,70,0.7) 55%, rgba(120,160,70,0) 100%),
      radial-gradient(ellipse 47% 40% at 50% 60%, #de3b43 0%, #d8353d 55%, rgba(222,70,75,0.55) 80%, rgba(222,70,75,0) 100%);
  }
  .label--blueberry .fruit-art {
    left: 160px; top: 14px; width: 112px; height: 128px;
    background:
      radial-gradient(ellipse 20% 16% at 82% 20%, rgba(90,160,70,0.9) 0%, rgba(90,160,70,0) 100%),
      radial-gradient(ellipse 48% 46% at 50% 52%, #3d6cbd 0%, #4a7dc9 55%, rgba(90,130,200,0.5) 80%, rgba(90,130,200,0) 100%);
  }

  .product-name { position: absolute; z-index: 2; left: 16px; top: 126px; font-family: "Sacramento", cursive; font-weight: 400; line-height: 1; white-space: nowrap; }
  .label--strawberry .product-name { color: var(--strawberry); font-size: 54px; }
  .label--blueberry .product-name { color: var(--blueberry); font-size: 49px; top: 130px; }

  .product-type { position: absolute; z-index: 2; right: 22px; top: 193px; font-size: 15.5px; font-weight: 400; letter-spacing: 0.9px; color: var(--brown); }

  .ingredients-ring { position: absolute; left: -12px; top: 234px; width: 200px; height: 200px; }

  .ingredients { position: absolute; left: 19px; width: 160px; top: 295px; text-align: center; font-size: 11px; line-height: 14.6px; letter-spacing: 0.3px; }
  .volume { position: absolute; left: 19px; width: 160px; top: 362px; text-align: center; font-size: 18px; font-weight: 600; letter-spacing: 0.8px; color: var(--brown); }

  .best-before { position: absolute; left: 265px; top: 337px; transform: translate(-50%, -50%) rotate(-90deg); font-size: 5.6px; white-space: nowrap; letter-spacing: 0.1px; }
  .label--blueberry .best-before { top: 324px; }

  .producer { position: absolute; left: 10px; top: 448px; font-size: 6px; line-height: 7.6px; color: var(--brown); white-space: nowrap; }

  .brand { position: absolute; left: 180px; top: 439px; display: flex; align-items: center; gap: 4px; }
  .brand-dot { width: 8px; height: 8px; border-radius: 50%; background: var(--brown); }
  .brand-name { font-size: 12px; font-weight: 600; color: var(--brown); }
</style>
</head>
<body>
  <div class="bleed-frame bleed-frame--strawberry"></div>
  <div class="bleed-frame bleed-frame--blueberry"></div>

  <section class="label label--strawberry">
    <div class="fruit-art" role="img" aria-label="Aquarell-Illustration einer Erdbeere"></div>
    <h1 class="product-name">Erdbeer</h1>
    <p class="product-type">FRUCHTAUFSTRICH</p>
    <svg class="ingredients-ring" viewBox="0 0 200 200" aria-hidden="true">
      <circle cx="111" cy="101" r="88" fill="var(--disc)"/>
      <circle cx="102" cy="98" r="94" fill="none" stroke="var(--ring)" stroke-width="3"/>
      <circle cx="106" cy="101" r="91" fill="none" stroke="var(--ring-soft)" stroke-width="2"/>
    </svg>
    <p class="ingredients">Zutaten:<br>Erdbeeren, Gelier-<br>zucker 2:1, Zitronensäure</p>
    <p class="volume">275ml</p>
    <p class="best-before">mindestens haltbar bis: siehe Boden</p>
    <p class="producer">Lindqvisthof Hofladen GbR . Bernd &amp; Carola Wessling<br>Obere Kastanienallee 17. 83719 Rainfeld</p>
    <div class="brand"><span class="brand-dot"></span><span class="brand-name">Lindqvisthof</span></div>
  </section>

  <section class="label label--blueberry">
    <div class="fruit-art" role="img" aria-label="Aquarell-Illustration von Heidelbeeren mit Blättern"></div>
    <h1 class="product-name">Heidelbeer</h1>
    <p class="product-type">FRUCHTAUFSTRICH</p>
    <svg class="ingredients-ring" viewBox="0 0 200 200" aria-hidden="true">
      <circle cx="102" cy="98" r="94" fill="none" stroke="var(--ring)" stroke-width="3"/>
      <circle cx="106" cy="101" r="91" fill="none" stroke="var(--ring-soft)" stroke-width="2"/>
    </svg>
    <p class="ingredients">Zutaten:<br>Heidelbeeren, Gelier-<br>zucker 2:1, Zitronensäure</p>
    <p class="volume">275ml</p>
    <p class="best-before">mindestens haltbar bis: siehe Boden</p>
    <p class="producer">Lindqvisthof Hofladen GbR . Bernd &amp; Carola Wessling<br>Obere Kastanienallee 17. 83719 Rainfeld</p>
    <div class="brand"><span class="brand-dot"></span><span class="brand-name">Lindqvisthof</span></div>
  </section>
</body>
</html>
```